Company Introduction/Advertisement Flyer

We would like to redesign our current company line card. We send this printed flyer to prospective customers to introduce our company, the brands we represent and our competitive advantages. Our current design is very plain and simple, we'd like to have a little more design to the new version. Our website is www.valvequarryhub.com. We're a specialty supplier for plumbing material, specifically water and life safety products. Our customers are mostly male, blue-collar contractors, ages 40-60. I have included a pdf of our current flyer, and our high resolution transparent logo.

Requirements
Must have
• Phone number: (800) 314-2760
Website: www.valvequarryhub.com

```html
<!DOCTYPE html>
<html lang="en">
<head>
<meta charset="utf-8">
<title>Summit Flowguard Supply Company – Line Card</title>
<link rel="stylesheet" href="https://fonts.googleapis.com/css2?family=Montserrat:wght@600;700;800;900&family=Open+Sans:wght@400;600;700&display=swap">
<style>
  :root{
    --navy:#1c3f8f;
    --blue:#2457b8;
    --sky:#4a86d6;
    --red:#e0343b;
    --ink:#2b2f3a;
    --muted:#6b7382;
    --paper:#ffffff;
    --line:#d9dee8;
  }
  *{box-sizing:border-box;margin:0;padding:0}
  html,body{width:1200px;height:2300px;overflow:hidden;background:var(--paper)}
  body{font-family:"Open Sans",Arial,sans-serif;color:var(--ink);position:relative}
  .flyer{position:relative;width:1200px;height:2300px;overflow:hidden;background:var(--paper)}

  .corner-band{position:absolute;top:0;right:0}

  .brand{position:absolute;left:70px;top:70px;display:flex;align-items:center;gap:18px}
  .brand-mark{width:54px;height:54px;background:var(--red);border-radius:50%}
  .brand-name{font-family:"Montserrat",Arial,sans-serif;font-weight:700;color:var(--navy);font-size:40px;line-height:1.05}
  .brand-name small{display:block;font-size:22px;font-weight:700;color:var(--navy);letter-spacing:.5px}

  .headline{position:absolute;left:70px;top:310px;width:560px;font-family:"Montserrat",Arial,sans-serif;font-weight:900;line-height:1.05;font-size:48px;white-space:nowrap}
  .headline .line-a{color:var(--navy);display:block}
  .headline .line-b{color:var(--red);display:block;font-size:62px}
  .sub{position:absolute;left:70px;top:480px;width:520px;font-family:"Montserrat",Arial,sans-serif;font-weight:600;color:var(--sky);font-size:32px;line-height:1.3}

  .hero{position:absolute;left:660px;top:230px}

  .services-title{position:absolute;left:70px;top:800px;font-family:"Montserrat",Arial,sans-serif;font-weight:800;color:var(--navy);font-size:46px;line-height:1.15}

  .advantages{position:absolute;left:70px;top:960px;width:560px;list-style:none}
  .advantages li{display:flex;align-items:center;gap:24px;height:92px;border-bottom:1px solid var(--line);font-size:24px;font-weight:600;color:var(--ink);line-height:1.3}
  .advantages .dot{flex:0 0 58px;height:58px;border-radius:50%;background:var(--red);display:flex;align-items:center;justify-content:center}

  .side-photos{position:absolute;left:680px;top:900px}

  .partners{position:absolute;left:70px;top:1660px;width:560px;display:grid;grid-template-columns:repeat(4,1fr);gap:26px 22px}
  .partner-badge{height:50px;border-radius:8px;background:#e6eaf2}
  .partner-badge.alt{background:#d3dbe9}

  .product-strip{position:absolute;left:70px;top:1900px;width:560px;height:190px;border-radius:10px;background:linear-gradient(90deg,#b8c3d6,#8fa0bd 40%,#c9d1df 70%,#9aa9c2)}

  .footer{position:absolute;left:0;bottom:0;width:1200px;height:110px;background:var(--navy);display:flex;align-items:center;color:#fff;font-size:24px;font-weight:600;padding-left:70px;gap:60px}
  .footer .cta{margin-left:auto;height:110px;width:380px;background:var(--red);display:flex;align-items:center;justify-content:center;font-family:"Montserrat",Arial,sans-serif;font-weight:700;font-size:24px}
</style>
</head>
<body>
<main class="flyer">

  <svg class="corner-band" width="560" height="200" viewBox="0 0 560 200" aria-hidden="true">
    <polygon points="160,0 560,0 560,90 300,90" fill="#1c3f8f"/>
    <polygon points="320,100 560,100 560,120 340,120" fill="#e0343b"/>
  </svg>

  <header class="brand">
    <span class="brand-mark"></span>
    <div class="brand-name">Summit Flowguard<small>Supply Company</small></div>
  </header>

  <h1 class="headline"><span class="line-a">YOUR COMPLETE</span><span class="line-b">SOURCE FOR</span></h1>
  <p class="sub">Backflow Prevention Repair Parts Accessories</p>

  <svg class="hero" width="540" height="560" viewBox="0 0 540 560">
    <defs>
      <linearGradient id="warehouse" x1="0" y1="0" x2="1" y2="1">
        <stop offset="0" stop-color="#c9a77a"/>
        <stop offset=".55" stop-color="#8b9bb4"/>
        <stop offset="1" stop-color="#d9773f"/>
      </linearGradient>
    </defs>
    <polygon points="90,0 540,0 540,560 0,560 0,120" fill="#2457b8"/>
    <polygon points="104,14 540,14 540,546 14,546 14,128" fill="url(#warehouse)" role="img" aria-label="Warehouse aisle with stocked shelves and orange ladder"/>
  </svg>

  <h2 class="services-title">Enclosures Test<br>Gauge Calibration</h2>

  <ul class="advantages">
    <li><span class="dot"><svg width="28" height="28" viewBox="0 0 24 24"><path d="M4 12l5 5L20 6" stroke="#fff" stroke-width="3" fill="none"/></svg></span>Next day part shipping straight to your doorstep</li>
    <li><span class="dot"><svg width="28" height="28" viewBox="0 0 24 24"><path d="M4 12l5 5L20 6" stroke="#fff" stroke-width="3" fill="none"/></svg></span>1-2 day delivery anywhere in the country</li>
    <li><span class="dot"><svg width="28" height="28" viewBox="0 0 24 24"><path d="M4 12l5 5L20 6" stroke="#fff" stroke-width="3" fill="none"/></svg></span>Friendly knowledgeable staff</li>
    <li><span class="dot"><svg width="28" height="28" viewBox="0 0 24 24"><path d="M4 12l5 5L20 6" stroke="#fff" stroke-width="3" fill="none"/></svg></span>No minimum orders</li>
    <li><span class="dot"><svg width="28" height="28" viewBox="0 0 24 24"><path d="M4 12l5 5L20 6" stroke="#fff" stroke-width="3" fill="none"/></svg></span>Same day shipping</li>
    <li><span class="dot"><svg width="28" height="28" viewBox="0 0 24 24"><path d="M4 12l5 5L20 6" stroke="#fff" stroke-width="3" fill="none"/></svg></span>Online tracking of your order</li>
    <li><span class="dot"><svg width="28" height="28" viewBox="0 0 24 24"><path d="M4 12l5 5L20 6" stroke="#fff" stroke-width="3" fill="none"/></svg></span>Technicians available to answer questions</li>
  </ul>

  <svg class="side-photos" width="520" height="960" viewBox="0 0 520 960">
    <defs>
      <linearGradient id="pipe" x1="0" y1="0" x2="1" y2="1"><stop offset="0" stop-color="#a8845a"/><stop offset="1" stop-color="#5c6d86"/></linearGradient>
      <linearGradient id="valve" x1="0" y1="0" x2="1" y2="0"><stop offset="0" stop-color="#b58a52"/><stop offset="1" stop-color="#7d8aa0"/></linearGradient>
      <linearGradient id="tech" x1="0" y1="0" x2="0" y2="1"><stop offset="0" stop-color="#8fb1d9"/><stop offset="1" stop-color="#d9a441"/></linearGradient>
    </defs>
    <polygon points="70,0 520,0 520,280 0,280 0,70" fill="#2457b8"/>
    <polygon points="80,10 520,10 520,270 10,270 10,78" fill="url(#pipe)" role="img" aria-label="Brass backflow valve installed on piping"/>
    <polygon points="70,330 520,330 520,610 0,610 0,400" fill="#2457b8"/>
    <polygon points="80,340 520,340 520,600 10,600 10,408" fill="url(#valve)" role="img" aria-label="Close view of backflow preventer repair parts"/>
    <polygon points="70,660 520,660 520,940 0,940 0,730" fill="#2457b8"/>
    <polygon points="80,670 520,670 520,930 10,930 10,738" fill="url(#tech)" role="img" aria-label="Technician in hard hat at work site"/>
  </svg>

  <div class="partners" aria-label="Represented brands">
    <span class="partner-badge"></span><span class="partner-badge alt"></span><span class="partner-badge"></span><span class="partner-badge alt"></span>
    <span class="partner-badge alt"></span><span class="partner-badge"></span><span class="partner-badge alt"></span><span class="partner-badge"></span>
    <span class="partner-badge"></span><span class="partner-badge alt"></span><span class="partner-badge"></span><span class="partner-badge alt"></span>
  </div>

  <div class="product-strip" role="img" aria-label="Row of backflow preventer assemblies"></div>

  <footer class="footer">
    <span>Daily Ph: (800) 314-2760</span>
    <span>24 hour Fax: (800) 314-2799</span>
    <span class="cta">www.valvequarryhub.com</span>
  </footer>
</main>
</body>
</html>
```